Updated flyer

We've decided to do this as a house party, the info is below. For this you can use a model or not use one, either way is fine. I attached two logos and some designs we've used from sketch hive before. I also attached a pic with a duck that you can use as the background
RUN WILD
(Pool Party Edition)
July 13 2013
Featuring DJs
Marlo (logo) Tevan (logo)
Neil Hartwick Marcus Obreno
meetwallz.com/marlo87 for address (Natomas, invite only)
Full Bar/Food/Water Basketball/Pool Table/Fun
Reason: I changed the info since it's a house party now so I didn't want to rush to close. It is a guaranteed project though thx
21-40 year old house music lounge lovers
House

```html
<!DOCTYPE html>
<html lang="en">
<head>
<meta charset="utf-8">
<title>Run Wild – Pool Party Edition</title>
<link rel="stylesheet" href="https://fonts.googleapis.com/css2?family=Chewy&family=Righteous&family=Crimson+Pro:wght@600&display=swap">
<style>
  :root {
    --page-bg: #e4e4e4;
    --band: #264f63;
    --band-deep: #1f4354;
    --ink: #17252e;
    --sky: #8ec9ea;
    --sky-light: #b9def2;
    --skin: #d6bcae;
    --title-top: #d8f0ff;
    --title-bottom: #2b86c4;
    --white: #ffffff;
  }
  * { margin: 0; padding: 0; box-sizing: border-box; }
  html, body {
    width: 1200px; height: 900px; overflow: hidden;
    background: var(--page-bg);
  }
  .flyer {
    position: absolute; left: 294px; top: 20px;
    width: 612px; height: 860px;
    background: var(--band);
    overflow: hidden;
    box-shadow: 0 6px 18px rgba(0,0,0,.35);
  }
  .hero-photo {
    position: absolute; left: 0; top: 0; width: 612px; height: 620px;
    background:
      radial-gradient(ellipse 260px 300px at 190px 230px, var(--skin) 0%, rgba(214,188,174,.6) 45%, rgba(214,188,174,0) 75%),
      linear-gradient(100deg, #6f98a8 0%, var(--sky) 45%, var(--sky-light) 80%, var(--sky) 100%);
  }
  .crowd {
    position: absolute; left: 0; top: 560px; width: 612px; height: 70px;
    background: linear-gradient(180deg, rgba(38,79,99,0) 0%, rgba(38,79,99,.85) 45%, var(--band) 100%);
  }
  .lineup {
    position: absolute; left: 360px; top: 0; width: 250px;
    text-align: center; color: var(--ink);
  }
  .featuring {
    position: absolute; top: 118px; width: 100%;
    font: 600 17px "Crimson Pro", serif; letter-spacing: 1px;
  }
  .act { position: absolute; width: 100%; }
  .act-tevan { top: 148px; }
  .act-tevan .mark {
    width: 106px; height: 106px; border-radius: 50%;
    margin: 0 auto; background: #4f9fc6;
    display: flex; align-items: center; justify-content: center;
    font: 26px "Righteous", sans-serif; color: var(--ink);
  }
  .act-marlo { top: 292px; font: 42px "Righteous", sans-serif; letter-spacing: 2px; line-height: 1; }
  .genres {
    position: absolute; top: 338px; width: 100%;
    font: 12px "Righteous", sans-serif; letter-spacing: .5px;
  }
  .djs {
    position: absolute; top: 366px; width: 100%;
    font: 24px "Righteous", sans-serif; line-height: 1.25;
  }
  .web {
    position: absolute; top: 433px; width: 100%;
    font: 600 16px "Crimson Pro", serif; letter-spacing: .5px;
  }
  .amenities {
    position: absolute; top: 470px; width: 100%;
    font: 600 17px "Crimson Pro", serif; line-height: 1.25; letter-spacing: .5px;
  }
  .headline {
    position: absolute; left: 0; top: 640px; width: 612px; text-align: center;
  }
  .title {
    font: 96px "Chewy", cursive; line-height: 1; letter-spacing: 3px;
    background: linear-gradient(180deg, var(--title-top) 0%, #7cc3ef 45%, var(--title-bottom) 100%);
    -webkit-background-clip: text; background-clip: text; color: transparent;
    -webkit-text-stroke: 2px var(--white);
  }
  .edition {
    margin-top: 12px; font: 36px "Chewy", cursive; color: var(--white); line-height: 1;
  }
  .date {
    margin-top: 12px; font: 38px "Chewy", cursive; color: var(--white); letter-spacing: 1px; line-height: 1;
  }
</style>
</head>
<body>
  <main class="flyer">
    <div class="hero-photo" role="img" aria-label="Photo of a model with turquoise eye makeup beside a mirrored disco ball, with palm leaves at the top corners"></div>
    <div class="crowd" role="img" aria-label="Silhouette of a dancing crowd with raised hands"></div>

    <section class="lineup">
      <p class="featuring">FEATURING</p>
      <div class="act act-tevan"><div class="mark">Tevan</div></div>
      <p class="act act-marlo">MARLO</p>
      <p class="genres">house · garage · 2step</p>
      <p class="djs">Neil Hartwick<br>Marcus Obreno</p>
      <p class="web">MEETWALLZ.COM/MARLO87</p>
      <p class="amenities">FULL BAR / FOOD /<br>WATER BASKETBALL /<br>POOL TABLE / FUN</p>
    </section>

    <section class="headline">
      <h1 class="title">RUN WILD</h1>
      <p class="edition">(Pool Party Edition)</p>
      <p class="date">July 13 2013</p>
    </section>
  </main>
</body>
</html>
```